2 x Digitize Logo | 2 x Business Cards | 2 x Fridge Magnets

We require 6 deliverables:
1. Residential logo redrawn (same just high quality for large print format).
2. Corporate logo redrawn (minor changes to wording and high quality for large print format).
3. New business card design for Furniture Removals (residential)
4. New business card design for Corporate Relocations (business)
5. New Fridge magnet for Furniture removals (residential)
6. New fridge magnet for Corporate Relocations (business)
1. Residential Logo
a. We require the logo to be translated into a high quality digital image with no modifications.
(see attached resilogo.jpg)
2. Residential Logo
a. We require the logo to be edited (add the word corporate relocations) be translated into a high quality digital image.
(see attached corplogo.jpg)
3. Using the resilogo please make a new business card for our business.
a. Please see the web site https://www.bluegatehaulage.com.au for colours and inspiration.
b. The residential business card needs the following information:
i. Business Name (using the residential logo).
ii. Free Call: 1800 BG Haul (the B, G and Haul much be the same colour as the logo).
iii. Website: www.BluegateHaulage.com.au
iv. Address: 4/6 Marlow Court, VIC 3201
v. Email: move@BluegateHaulage.com.au
vi. backof Card:
Review our service
www.TellTallyHub.com.au
Services: Local, Country, Interstate | Furniture Removals | Piano, Billiard Tables & Antiques
4. Using the corplogo please make a new business card for our business.
b. The corporate business card needs the following information:
i. Business Name (using the corporate logo).
v. Email: corporate@BluegateHaulage.com.au
vi. Back of Card:
Review our service
www.TellTallyHub.com.au
Services: Corporate relocations | Office equipment moves | Packing Service | Packing Materials
5. Using the resilogo please make a new fridge magent for our business.
b. The residential fidge magnet needs the following information:
iv. Services: Local, Country, Interstate | Furniture Removals | Piano, Billiard Tables & Antiques
6. Using the corplogo please make a new fridge magent for our business.
b. The corporate fidge magnet needs the following information:
iv. Services: Local, Country, Interstate | Corporate relocations
Target Market(s)
Residential Furniture Removals and Corporate Office relocations
Industry/Entity Type
Business
Contact Information for Business Card
Please see full brief for six items required
Requirements
Must have
- Clean simple, easy to read
Nice to have
- fresh, stand out, eye catching
Should not have
- plain, standard, boring, general

```html
<!DOCTYPE html>
<html lang="en">
<head>
<meta charset="utf-8">
<title>Bluegate Haulage – Business Card</title>
<link rel="stylesheet" href="https://fonts.googleapis.com/css2?family=Archivo+Black&family=Arimo:wght@400;700&display=swap">
<style>
  :root {
    --backdrop: #ababab;
    --shadow: #595959;
    --card: #ffffff;
    --ink: #000000;
    --yellow: #ffc815;
    --red: #ed1c24;
    --green: #22b14c;
  }
  * { margin: 0; padding: 0; box-sizing: border-box; }
  html, body { width: 1200px; height: 800px; overflow: hidden; }
  body { background: var(--backdrop); position: relative; font-family: "Arimo", Arial, sans-serif; color: var(--ink); }

  .card {
    position: absolute;
    width: 480px;
    height: 320px;
    background: var(--card);
    box-shadow: 19px 19px 0 var(--shadow);
    overflow: hidden;
  }
  .card--front { left: 81px; top: 69px; }
  .card--back { left: 617px; top: 398px; text-align: center; }

  .brand {
    position: absolute;
    left: 0; right: 0; top: 112px;
    height: 56px;
    display: flex; align-items: center; justify-content: center; gap: 12px;
    font-family: "Archivo Black", "Arial Black", sans-serif;
    font-size: 38px;
    letter-spacing: -0.5px;
    color: var(--green);
    text-transform: uppercase;
  }
  .brand__dot { width: 18px; height: 18px; border-radius: 50%; background: var(--red); }
  .card--front .brand { top: 43px; }

  .freecall {
    position: absolute;
    left: 0; right: 0; top: 123px;
    font-family: "Archivo Black", "Arial Black", sans-serif;
    font-size: 31px;
    text-align: center;
    line-height: 1;
  }
  .c-yellow { color: var(--yellow); }
  .c-red { color: var(--red); }
  .c-green { color: var(--green); }

  .info-band {
    position: absolute;
    left: 0; right: 0;
    height: 47px;
    display: flex; align-items: center; justify-content: center;
    font-size: 21px;
  }
  .info-band--web { top: 177px; background: var(--yellow); }
  .info-band--address { top: 224px; background: var(--red); }
  .info-band--email { top: 271px; height: 49px; background: var(--green); }

  .review__title {
    margin-top: 34px;
    font-family: "Archivo Black", "Arial Black", sans-serif;
    font-size: 37px;
    line-height: 1;
  }
  .review__url {
    margin-top: 4px;
    font-family: "Archivo Black", "Arial Black", sans-serif;
    font-size: 21px;
    line-height: 1;
    padding-right: 16px;
  }
  .services {
    margin-top: 64px;
    font-family: "Archivo Black", "Arial Black", sans-serif;
    font-size: 21px;
    line-height: 27px;
    letter-spacing: 0.2px;
  }
  .services__label { font-family: "Arimo", Arial, sans-serif; font-weight: 400; }
</style>
</head>
<body>
  <section class="card card--front" aria-label="Business card front">
    <div class="brand"><span class="brand__dot"></span><span class="brand__name">Bluegate Haulage</span></div>
    <p class="freecall">Free Call: 1800 <span class="c-yellow">B</span><span class="c-red">G</span> <span class="c-green">Haul</span></p>
    <p class="info-band info-band--web">Website: www.BluegateHaulage.com.au</p>
    <p class="info-band info-band--address">Address: 4/6 Marlow Court, VIC 3201</p>
    <p class="info-band info-band--email">Email: move@BluegateHaulage.com.au</p>
  </section>

  <section class="card card--back" aria-label="Business card back">
    <h2 class="review__title">Review our service</h2>
    <p class="review__url">www.TellTallyHub.com.au</p>
    <p class="services">
      <span class="services__label">Services:</span>
      <span class="c-yellow">Local,</span> <span class="c-red">Country,</span> <span class="c-green">Interstate |</span><br>
      <span class="c-red">Furniture</span> <span class="c-green">Removals</span> <span class="c-yellow">| Piano,</span> <span class="c-red">Billiard</span><br>
      <span class="c-yellow">Tables</span> <span class="c-red">&amp; Antiques</span>
    </p>
  </section>
</body>
</html>
```